Pruett Design & Millwork needs a web presence. Looking for a unique Design so please submit an idea.

In brief, you should know the following about me: My company was established in 2001 and had been responsible for providing reasonable CAD Design and Custom Millwork ever since. My specialty is in the area Architectural CAD Design, Fabrication of Custom Millwork and Mouldings on a partime basis. Drawings and estimates done at a very reasonable cost. I look forward to working on your next project. Thanks in Advance, Glen 
I would like one page to show thumbnails linked to some of past millwork projects and another page with thumbnails linking to some of my house designs. I assume last page will have contact information accessed from a link on home page. I already had a logo designed which I can supply you with to design home page around. As I indicated I have a regular full time job and do this for additional income and will move to full time when I have enough business.

I have attached the logo I had designed in a couple different colors. I have also uploaded some PDF's of files that I also considered before choosing the RED LOGO to give an ideas of how we could tweak the logo to better fit the website if need be. Text is wrong in those.

Thanks,
Glen

I added my logo as a PDF side there seems to be a problem with scaling loge with the other file. Hope this helps.

Glen

Evening,
I will be hosting this site on servquill. Its looks like it will get launched with wordpress?  What will be involved from getting your design up so I can upload project pictures and and text to areas you have set aside? I am also going to upload a couple jpg of a couple recent projects so you can put in so I can get a feel of what they will look like. Thanks for all your work to date! Glen

I am not seeing alot of design variations or even many designers in fact. Is there something more from me you need? Do you need me to extend deadline?

Reason: It appears that your need some more time to submit some design changes. I will choose a design next week after changes have been submitted. Thanks for your time. Glen

Reason: Designers needs a couple days to submit some last minute changes. Thanks for all your submissions! Glen

Reason: Some last minute designs that I need to look at and give feedback on. I want to thank everyone for their designs and patience. Thanks again, Glen

Evening All,

Upon discussion with a couple of the designers I want the design done in Word Press and I have increased budget the amount they said they would need to do it for. Thanks for all submissions so far but I am still looking for the special one that stands out among the rest! Glen

I will not be extending deadline and choosing designer tomorrow morning so if you have anything else to add please do so tonight. Thanks for all your submissions. Glen

Target Market(s)

Millwork projects will be generally local where as CAD Design Projects could be emailed anywhere. Probably more USA but who knows.

Industry/Entity Type

House

Font styles to use
Other font styles liked:
• Eras Medium ITC, Calibri or Designers choice.

Requirements
Must have
• Must tie in my logo on Homepage at least. Could even be somewhat transparent in background? I will let the designer work that out.
Nice to have
• Page to point to current and past Design projects on one page and millwork on another.
Should not have
• Target a large Corporate or Global environment since it is a small business right now.

```html
<!DOCTYPE html>
<html lang="en">
<head>
<meta charset="utf-8">
<title>Pruett Design &amp; Millwork</title>
<link href="https://fonts.googleapis.com/css2?family=Open+Sans:ital,wght@0,400;0,600;0,700;1,400&display=swap" rel="stylesheet">
<style>
:root{
  --red:#cc0f14;
  --ink:#111;
  --text:#444;
  --muted:#8a8a8a;
  --line:#e2e2e2;
  --panel:#f3f3f3;
  --footer:#ececec;
  --bar:#2b2626;
  --white:#fff;
  --wood-dark:#6b3414;
  --wood:#b8682b;
  --wood-light:#e7c18c;
}
*{margin:0;padding:0;box-sizing:border-box}
html,body{width:684px;height:1200px;overflow:hidden}
body{font-family:"Open Sans",Arial,sans-serif;color:var(--text);background:var(--white);position:relative}
.abs{position:absolute}
a{color:inherit;text-decoration:none}

/* header */
.site-header{left:0;top:0;width:684px;height:50px;background:var(--white);border-bottom:2px solid var(--red);z-index:3}
.brand{left:85px;top:0;width:84px;height:76px;background:var(--white);box-shadow:0 2px 5px rgba(0,0,0,.25);z-index:4;display:flex;flex-direction:column;align-items:center;justify-content:center;gap:4px}
.brand-mark{width:14px;height:14px;background:var(--red)}
.brand-name{font-size:7px;font-weight:700;color:var(--red);text-align:center;line-height:1.15}
.main-nav{right:77px;top:0;height:48px;display:flex;z-index:4}
.main-nav a{display:block;padding:0 8px;line-height:52px;font-size:7.5px;font-weight:700;color:#333}
.main-nav a.is-active{color:var(--red);background:#f0f0f0}

/* hero */
.hero{left:0;top:50px;width:684px;height:338px;background:linear-gradient(100deg,#e9edd2 0%,#f4e8c8 22%,var(--wood) 40%,var(--wood-dark) 55%,#c98a4e 72%,#8f4a1e 100%)}
.hero-arrow{top:206px;width:29px;height:29px;border-radius:50%;background:rgba(60,60,60,.7);z-index:2}
.hero-arrow svg{display:block;margin:8px auto}
.thumbs{left:86px;top:361px;z-index:2}
.thumb{position:absolute;top:0;width:120px;height:81px;border:3px solid var(--white);box-shadow:0 1px 4px rgba(0,0,0,.3)}
.thumb.is-current{border-color:var(--red)}

/* welcome */
.welcome-title{left:0;top:466px;width:684px;text-align:center;font-size:15px;font-weight:700;color:var(--ink)}
.welcome-title span{color:var(--red)}
.welcome-text{left:82px;top:491px;width:520px;text-align:center;font-size:6.6px;line-height:12.8px;color:#555}

/* updates band */
.updates{left:0;top:565px;width:684px;height:261px;background:var(--panel)}
.section-title{font-size:14px;font-weight:700;color:var(--ink);white-space:nowrap;display:flex;align-items:center}
.section-title em{font-style:normal;color:var(--red);margin-left:4px}
.section-title small{font-size:5.5px;font-weight:400;color:var(--muted);margin-left:3px;padding-top:5px}
.title-rule{height:5px;background:#e4e4e4}
.post-title{font-size:7.6px;font-weight:700;color:#333}
.post-text{font-size:6.6px;line-height:11px;color:#555}
.avatar{width:40px;height:40px;border:2px solid var(--white);box-shadow:0 0 2px rgba(0,0,0,.3);background:linear-gradient(160deg,#6b4a36,#e8cdb9 60%,#fafafa)}
.meta{font-size:6px;color:var(--muted);display:flex;align-items:center;gap:4px}
.divider{height:1px;background:var(--line)}
.date-box{width:43px;height:44px;background:#c6c6c6;color:var(--white);text-align:center;font-weight:700}
.date-box b{display:block;font-size:15px;line-height:18px;padding-top:4px}
.date-box i{display:block;font-style:normal;font-size:9px;line-height:12px;border-top:1px solid #ddd;margin:2px 4px 0}
.more{font-size:6px;color:#333;display:flex;align-items:center;gap:4px}
.button-ghost{height:16px;padding:0 6px;background:#dedede;font-size:5.8px;font-weight:600;color:#555;line-height:16px}

/* house designs */
.design-card{top:878px;width:120px;height:126px;border:1px solid var(--line);background:var(--white);padding:3px}
.design-card .pic{height:78px}
.design-card .caption{background:#f5f5f5;height:40px;padding:6px 7px;font-size:7px;color:#333}
.design-card .caption p+p{font-size:6px;color:var(--muted);margin-top:5px;display:flex;align-items:center;gap:3px}

/* footer */
.site-footer{left:0;top:1030px;width:684px;height:141px;background:var(--footer)}
.footer-title{font-size:8.6px;font-weight:700;color:#222}
.quick-links{list-style:none;font-size:6.8px;line-height:12.8px;color:#333}
.vrule{width:1px;background:#d4d4d4}
.quote{font-size:6.8px;line-height:12.5px;color:#555}
.quote-name{font-size:6.8px;color:var(--red)}
.news-input{width:104px;height:19px;background:var(--white);border:1px solid #ddd;font-size:6.2px;color:var(--muted);padding:5px 10px}
.news-submit{width:43px;height:19px;background:var(--red);color:var(--white);font-size:7.4px;font-weight:600;text-align:center;line-height:19px}
.social{top:1136px;width:16px;height:16px}
.bottom-bar{left:0;top:1171px;width:684px;height:29px;background:var(--bar);color:#ddd;font-size:6.8px;text-align:center;line-height:29px}
</style>
</head>
<body>

<header class="abs site-header"></header>
<a class="abs brand" href="#">
  <span class="brand-mark"></span>
  <span class="brand-name">Pruett Design<br>&amp; Millwork</span>
</a>
<nav class="abs main-nav">
  <a class="is-active" href="#">HOME</a><a href="#">ABOUT</a><a href="#">SERVICES</a><a href="#">PORTFOLIO</a><a href="#">BLOG</a><a href="#">NEWS</a><a href="#">CONTACT</a>
</nav>

<section class="abs hero" role="img" aria-label="Photo of a warm wooden kitchen with a granite island and a breakfast table"></section>
<a class="abs hero-arrow" style="left:14px" href="#"><svg width="10" height="13" viewBox="0 0 10 13"><path d="M8 1 2 6.5 8 12" fill="none" stroke="#fff" stroke-width="2.4"/></svg></a>
<a class="abs hero-arrow" style="left:636px" href="#"><svg width="10" height="13" viewBox="0 0 10 13"><path d="M2 1 8 6.5 2 12" fill="none" stroke="#fff" stroke-width="2.4"/></svg></a>

<div class="abs thumbs">
  <div class="thumb" style="left:0;background:linear-gradient(135deg,#3a4a7a,#8a5a2a 60%,#2c2a4a)" role="img" aria-label="Game room with billiard table"></div>
  <div class="thumb is-current" style="left:131px;background:linear-gradient(135deg,#f0e2c0,#b0602a 50%,#7a3a18)" role="img" aria-label="Wooden kitchen"></div>
  <div class="thumb" style="left:262px;background:linear-gradient(135deg,#e8d8a8,#8a6a3a 50%,#3a2a1a)" role="img" aria-label="Living room with sofas"></div>
  <div class="thumb" style="left:392px;background:linear-gradient(135deg,#4a5a8a,#7a4a2a 55%,#2a2a4a)" role="img" aria-label="Game room with fireplace"></div>
</div>

<h1 class="abs welcome-title">Welcome to <span>PruettDesign and Millwork</span></h1>
<p class="abs welcome-text">Lorem ipsum dolor sit amet, consectetur adipiscing elit. Duis auctor erat eget lobortis dictum. Mauris dolor felis, rutrum quis elit ut, adipiscing accumsan nulla. Suspendisse neque velit, faucibus quis imperdiet a, blandit sit amet dolor. Duis nec sollicitudin erat. Nulla sed elementum tortor. Curabitur sed auctor augue. Nunc et purus diam. Etiam ac elit urna. Sed vitae feugiat magna. Donec ullamcorper lectus erat, vitae viverra massa lobortis ut. Integer sodales orci nunc, in laoreet ipsum consectetur sit amet. Praesent ante nunc, congue at justo vitae, convallis blandit nisi.</p>

<section class="abs updates"></section>

<!-- featured blog -->
<h2 class="abs section-title" style="left:85px;top:589px">Featured<em>Blog</em><small>get latest updates</small></h2>
<div class="abs title-rule" style="left:235px;top:598px;width:93px"></div>

<div class="abs avatar" style="left:86px;top:622px" role="img" aria-label="Author portrait"></div>
<p class="abs post-title" style="left:137px;top:620px">Lorem ipsum dolor am consectetur adipiscing</p>
<p class="abs post-text" style="left:137px;top:635px;width:190px">Lorem ipsum dolor sit amet, consectetur adipiscing Duis auctor erat eget lobortis dictum. Mauris dolor felis....</p>
<div class="abs meta" style="left:205px;top:671px">
  <svg width="7" height="7" viewBox="0 0 7 7"><rect x=".5" y="1" width="6" height="5.5" fill="none" stroke="#999"/><path d="M.5 3h6" stroke="#999"/></svg>10 Feb, 2014
  <svg style="margin-left:8px" width="8" height="7" viewBox="0 0 8 7"><path d="M1 1h6v4H3L1 6.5z" fill="#aaa"/></svg>12 Comments
</div>
<div class="abs divider" style="left:85px;top:690px;width:243px"></div>

<div class="abs avatar" style="left:86px;top:704px" role="img" aria-label="Author portrait"></div>
<p class="abs post-title" style="left:137px;top:702px">Lorem ipsum dolor am consectetur adipiscing</p>
<p class="abs post-text" style="left:137px;top:717px;width:190px">Lorem ipsum dolor sit amet, consectetur adipiscing Duis auctor erat eget lobortis dictum. Mauris dolor felis....</p>
<div class="abs meta" style="left:205px;top:753px">
  <svg width="7" height="7" viewBox="0 0 7 7"><rect x=".5" y="1" width="6" height="5.5" fill="none" stroke="#999"/><path d="M.5 3h6" stroke="#999"/></svg>10 Feb, 2014
  <svg style="margin-left:8px" width="8" height="7" viewBox="0 0 8 7"><path d="M1 1h6v4H3L1 6.5z" fill="#aaa"/></svg>12 Comments
</div>
<a class="abs button-ghost" style="left:85px;top:783px" href="#">Show All Blog</a>

<!-- news feed -->
<h2 class="abs section-title" style="left:354px;top:589px">News<em>Feed</em><small>get latest updates</small></h2>
<div class="abs title-rule" style="left:486px;top:598px;width:112px"></div>

<div class="abs date-box" style="left:355px;top:617px"><b>10</b><i>FEB</i></div>
<p class="abs post-title" style="left:407px;top:616px">Lorem ipsum dolor am consectetur adipiscing</p>
<p class="abs post-text" style="left:407px;top:631px;width:190px">Lorem ipsum dolor sit amet, consectetur adipiscing Duis auctor erat eget lobortis dictum. Mauris dolor felis....</p>
<a class="abs more" style="left:528px;top:671px" href="#"><svg width="8" height="8" viewBox="0 0 8 8"><circle cx="4" cy="4" r="4" fill="#888"/><path d="M3 2.2 5.4 4 3 5.8z" fill="#fff"/></svg>Continue Reading...</a>

<div class="abs date-box" style="left:355px;top:702px"><b>10</b><i>FEB</i></div>
<p class="abs post-title" style="left:407px;top:701px">Lorem ipsum dolor am consectetur adipiscing</p>
<p class="abs post-text" style="left:407px;top:716px;width:190px">Lorem ipsum dolor sit amet, consectetur adipiscing Duis auctor erat eget lobortis dictum. Mauris dolor felis....</p>
<a class="abs more" style="left:528px;top:752px" href="#"><svg width="8" height="8" viewBox="0 0 8 8"><circle cx="4" cy="4" r="4" fill="#888"/><path d="M3 2.2 5.4 4 3 5.8z" fill="#fff"/></svg>Continue Reading...</a>
<a class="abs button-ghost" style="left:358px;top:783px" href="#">Show All&nbsp; News Feed</a>

<!-- house designs -->
<h2 class="abs section-title" style="left:85px;top:850px">My<em>House Designs</em></h2>

<div class="abs design-card" style="left:85px">
  <div class="pic" style="background:linear-gradient(135deg,#d8e0b0,#b0602a 50%,#6a3010)" role="img" aria-label="Kitchen design"></div>
  <div class="caption"><p>Lorem ipsum dolor amet</p><p><svg width="5" height="7" viewBox="0 0 5 7"><path d="M2.5 7 .3 3A2.3 2.3 0 1 1 4.7 3z" fill="#aaa"/></svg>Duis auctor erat</p></div>
</div>
<div class="abs design-card" style="left:216px">
  <div class="pic" style="background:linear-gradient(135deg,#5a2a18,#a8683a 50%,#d8b890)" role="img" aria-label="Kitchen with range hood"></div>
  <div class="caption"><p>Lorem ipsum dolor amet</p><p><svg width="5" height="7" viewBox="0 0 5 7"><path d="M2.5 7 .3 3A2.3 2.3 0 1 1 4.7 3z" fill="#aaa"/></svg>Duis auctor erat</p></div>
</div>
<div class="abs design-card" style="left:347px">
  <div class="pic" style="background:linear-gradient(135deg,#e8d8a8,#8a6a3a 50%,#3a2a1a)" role="img" aria-label="Living room design"></div>
  <div class="caption"><p>Lorem ipsum dolor amet</p><p><svg width="5" height="7" viewBox="0 0 5 7"><path d="M2.5 7 .3 3A2.3 2.3 0 1 1 4.7 3z" fill="#aaa"/></svg>Duis auctor erat</p></div>
</div>
<div class="abs design-card" style="left:478px">
  <div class="pic" style="background:linear-gradient(135deg,#4a5a8a,#7a4a2a 55%,#2a2a4a)" role="img" aria-label="Game room design"></div>
  <div class="caption"><p>Lorem ipsum dolor amet</p><p><svg width="5" height="7" viewBox="0 0 5 7"><path d="M2.5 7 .3 3A2.3 2.3 0 1 1 4.7 3z" fill="#aaa"/></svg>Duis auctor erat</p></div>
</div>

<!-- footer -->
<footer class="abs site-footer"></footer>
<h3 class="abs footer-title" style="left:85px;top:1048px">Quick Links</h3>
<ul class="abs quick-links" style="left:85px;top:1067px">
  <li>Home</li><li>About</li><li>Services</li><li>Portfolio</li><li>Blog</li><li>News</li><li>Contact</li>
</ul>
<div class="abs vrule" style="left:167px;top:1046px;height:112px"></div>

<h3 class="abs footer-title" style="left:192px;top:1048px">Testimonial</h3>
<svg class="abs" style="left:191px;top:1068px" width="12" height="12" viewBox="0 0 12 12"><path d="M1 11V6l3-5h2L4 6h2v5zM7 11V6l3-5h2l-2 5h2v5z" fill="#ccc"/></svg>
<p class="abs quote" style="left:205px;top:1070px;width:188px">Lorem ipsum dolor sit amet, consectetur adipiscing elit. Duis auctor erat eget lobortis dictum. Mauris dolor felis, rutrum quis elit ut, adipiscing accumsan nulla. Suspendisse neque velit, faucibus.</p>
<svg class="abs" style="left:318px;top:1110px" width="12" height="12" viewBox="0 0 12 12"><path d="M11 1v5l-3 5H6l2-5H6V1zM5 1v5l-3 5H0l2-5H0V1z" fill="#ccc"/></svg>
<p class="abs quote-name" style="left:197px;top:1130px">- Clients Name here</p>
<div class="abs vrule" style="left:418px;top:1046px;height:112px"></div>

<h3 class="abs footer-title" style="left:451px;top:1048px">Newsletter</h3>
<p class="abs quote" style="left:451px;top:1066px;width:150px">Lorem ipsum dolor sit amet, consectetur adipiscing elit. Duis auctor erat eget</p>
<div class="abs news-input" style="left:451px;top:1102px">Enter your e-mail</div>
<div class="abs news-submit" style="left:554px;top:1102px">SUBMIT</div>
<span class="abs social" style="left:451px;background:#3b5a98"></span>
<span class="abs social" style="left:474px;background:#2aa7e0"></span>
<span class="abs social" style="left:496px;background:#d63a2b"></span>
<span class="abs social" style="left:518px;background:#f08a1e"></span>

<div class="abs bottom-bar">© 2014 PruettDesign and Millwork. All rights reserved.</div>

</body>
</html>
```